COMMERCIAL REAL ESTATE FLYER TEMPLATE

We need a template flyer designed that we can use for a current commercial real estate listing and subsequently use as a template for future listings. We have uploaded images and files to provide an example of an older flyer template we have used. If you have questions or would like to discuss, please contact us at Wade@TLMVX.net. Colors selected should be in line with our attached business card and logo design. Output should be 8.5" X 11".

Target Market(s)

Commercial Real Estate. NO RESIDENTIAL. Needs to have a professional commercial presentation with no reference to residential real estate.

Industry/Entity Type

Real Estate Agent

Font styles to use
Serif

Colors

Designer to choose colors to be used in the design.

Requirements
Must have
• MUST BE SAVED AND ADJUSTABLE IN ONE OF THE FOLLOWING FORMATES: MICROSOFT POWERPOINT, PUBLISHER OR WORD. THIS IS IMPORTANT SO OUR TEAM CAN EASILLY UPDATE TEMPLATE IN READILLY AVAILABLE PROGRAMS THAT ARE SIMPLE FOR TEAM MEMBERS TO USE.
Nice to have
• Needs to have first page template with header and footer displaying our logo, address, phone, email address and contact information for the listing agent. There need to be placeholders that can be easily adjusted based on specific listings. Placeholders will be used for pictures or aerials as the case requires. Needs to have a second page that has header and footer with a clean open block in the middle of the page so agents can customize with site specific details.
Should not have
• There should be no reference to residential. We are a commercial real estate organization that does not do any residential.

```html
<!DOCTYPE html>
<html lang="en">
<head>
<meta charset="utf-8">
<title>Flex Industrial Listing Flyer</title>
<link href="https://fonts.googleapis.com/css2?family=Montserrat:wght@600;700&family=Questrial&display=swap" rel="stylesheet">
<style>
:root{
  --brand-red:#b8202a;
  --ink:#3a3a3a;
  --soft-ink:#8a8a8a;
  --paper:#ffffff;
  --stage:#e9e9e9;
  --office-blue:#aedde6;
  --warehouse-peach:#fbd3ae;
}
*{margin:0;padding:0;box-sizing:border-box}
html,body{width:1200px;height:1200px;overflow:hidden;background:var(--stage)}
body{position:relative;font-family:"Questrial",sans-serif;color:var(--ink)}
.page{position:absolute;top:242px;width:484px;height:663px;background:var(--paper);box-shadow:0 4px 14px rgba(0,0,0,.18);overflow:hidden}
.page--front{left:74px}
.page--details{left:618px;width:482px}
.header{position:absolute;left:0;top:0;width:100%;height:102px;background:var(--brand-red);color:#fff}
.header__title{position:absolute;left:35px;top:52px;font-family:"Montserrat",sans-serif;font-weight:700;font-size:9px;white-space:nowrap}
.header__address{position:absolute;left:35px;top:67px;font-size:8.6px;letter-spacing:.1px;white-space:nowrap}
.brand{position:absolute;right:32px;top:30px;display:flex;flex-direction:column;align-items:flex-end;gap:5px;font-family:"Montserrat",sans-serif;font-weight:700;color:#fff;text-align:right;line-height:1.05}
.brand__mark{width:26px;height:26px;background:#fff;margin-right:14px}
.brand__name{font-size:7.6px}
.brand__sub{font-size:5px;display:block}
.photo-frame{position:absolute;left:30px;top:90px;width:424px;height:245px;background:#fff;padding:3px;box-shadow:0 3px 6px rgba(0,0,0,.2)}
.photo{width:100%;height:100%;background:linear-gradient(180deg,#7fa8d8 0%,#cfdff0 42%,#b89a7c 62%,#6c8f3a 80%,#4f7a2a 100%)}
.feature-box{position:absolute;left:30px;top:354px;width:424px;height:129px;background:var(--brand-red);box-shadow:0 3px 6px rgba(0,0,0,.2)}
.map{position:absolute;left:3px;top:3px;width:238px;height:123px;background:linear-gradient(135deg,#eef0f2,#dfe4e8)}
.feature-box__text{position:absolute;left:244px;top:20px;width:178px;text-align:center;color:#fff;font-family:"Montserrat",sans-serif;font-weight:700;font-size:9.2px;line-height:12.6px}
.key-facts{position:absolute;left:0;top:501px;width:100%;text-align:center;font-size:11px;line-height:14.6px;letter-spacing:.2px}
.key-facts b{color:var(--brand-red);font-family:"Montserrat",sans-serif;font-weight:700}
.footer{position:absolute;left:30px;top:590px;width:424px;height:73px;background:var(--brand-red)}
.footer__card{position:absolute;left:0;top:0;width:424px;height:42px;background:#fff;display:flex;align-items:flex-start;padding:2px 6px}
.footer__badge{flex:none;width:56px;height:36px;background:var(--brand-red);color:#fff;font-family:"Montserrat",sans-serif;font-weight:700;font-size:5px;display:flex;flex-direction:column;align-items:center;justify-content:center;gap:3px;text-align:center;line-height:1.1}
.footer__badge span{width:9px;height:9px;background:#fff;display:block}
.footer__contact{flex:none;margin-left:6px;width:92px;font-size:4.9px;line-height:6.1px;font-family:"Montserrat",sans-serif;font-weight:600;color:#222}
.footer__contact b{color:var(--brand-red);font-weight:700}
.footer__legal{margin-left:6px;padding-left:5px;border-left:.6px solid #999;flex:1;font-size:4.7px;line-height:5.3px;color:#444}
.plan{position:absolute;left:30px;top:92px;width:254px;height:448px;background:#fff;padding:6px}
.plan__drawing{width:100%;height:100%;background:linear-gradient(180deg,var(--office-blue) 0%,var(--office-blue) 22%,var(--warehouse-peach) 30%,var(--warehouse-peach) 100%);border:1px solid #8aa}
.specs{position:absolute;left:292px;top:112px;width:180px;font-size:8.6px;line-height:11.7px;color:var(--soft-ink)}
.specs b{color:var(--brand-red);font-family:"Montserrat",sans-serif;font-weight:700;font-size:8px}
.specs__head{color:var(--brand-red);font-family:"Montserrat",sans-serif;font-weight:700;font-size:8px;margin-top:7px;margin-bottom:7px}
.specs ul{list-style:none}
.specs li{position:relative;padding-left:9px}
.specs li::before{content:"";position:absolute;left:0;top:4px;width:4px;height:4px;background:var(--brand-red)}
.plan-note{position:absolute;left:30px;top:554px;font-family:"Montserrat",sans-serif;font-weight:700;font-size:9.6px;color:var(--brand-red);white-space:nowrap}
</style>
</head>
<body>

<section class="page page--front">
  <header class="header">
    <div class="header__title">FLEX INDUSTRIAL FOR SALE OR LEASE - HOUSTON, TEXAS</div>
    <div class="header__address">4820 RIDGELINE INDUSTRIAL BLVD., HOUSTON, TEXAS 77099</div>
    <div class="brand"><span class="brand__mark"></span><span class="brand__name">TALMVEX<span class="brand__sub">COMMERCIAL REAL ESTATE</span></span></div>
  </header>
  <div class="photo-frame"><div class="photo" role="img" aria-label="Photo of the brick flex industrial building with monument sign and flower beds under a blue sky"></div></div>
  <div class="feature-box">
    <div class="map" role="img" aria-label="Area map showing the property location and nearby highways"></div>
    <div class="feature-box__text">FLEX INDUSTRIAL - FOR SALE OR LEASE WELL MAINTAINED<br>OWNER-OCCUPIED BUILDING<br>GREAT LOCATION<br>NEAR IAH &amp; THE WOODLANDS<br>EASY ACCESS TO HARDY,<br>IH-45 &amp; BELTWAY 8</div>
  </div>
  <div class="key-facts">
    <b>BUILDING AREA:</b> 11,820 SF (HCAD) I <b>LAND AREA:</b> 41,616 SF (HCAD)<br>
    <b>OFFICE BUILD-OUT:</b> APPROX. 2,820 SF (OWNER)<br>
    <b>LOADING:</b> THREE (3) GRADE-LEVEL<br>
    <b>EAVE HEIGHT:</b> APPROX. 22'<br>
    <b>OUTSIDE STORAGE: ROOM TO ADD FENCED YARD</b>
  </div>
  <footer class="footer">
    <div class="footer__card">
      <div class="footer__badge"><span></span>TALMVEX<br>COMMERCIAL REAL ESTATE</div>
      <div class="footer__contact"><b>WADE T. LORNE</b><br>PRESIDENT | CEO<br><b>PHONE:</b> (281) 555-0148<br><b>E-Mail:</b> Wade@TLMVX.net<br>TREC BROKER LICENSE: 9004417</div>
      <div class="footer__legal">The information contained herein was obtained from sources we believe to be reliable, and we have no reason to doubt its accuracy. All details are submitted subject to errors, omissions or changes in condition prior to sale, lease or withdrawal without notice. Buyers should verify all facts independently. We make no warranty regarding the condition of the property or any environmental matters.</div>
    </div>
  </footer>
</section>

<section class="page page--details">
  <header class="header">
    <div class="header__title">FLEX INDUSTRIAL FOR SALE OR LEASE - HOUSTON, TEXAS</div>
    <div class="header__address">4820 RIDGELINE INDUSTRIAL BLVD., HOUSTON, TEXAS 77099</div>
    <div class="brand"><span class="brand__mark"></span><span class="brand__name">TALMVEX<span class="brand__sub">COMMERCIAL REAL ESTATE</span></span></div>
  </header>
  <div class="plan"><div class="plan__drawing" role="img" aria-label="Interior floor plan with office rooms along the top and approximately 9,000 SF warehouse space below"></div></div>
  <div class="specs">
    <div><b>FLEX INDUSTRIAL</b> - FOR SALE OR LEASE</div>
    <div><b>Year of Construction:</b> 2006</div>
    <div><b>Building Area:</b> 11,820 SF (HCAD)</div>
    <div><b>Land Area:</b> 41,616 SF (HCAD)</div>
    <div><b>Approximate Office Area:</b> 2,820 SF (Owner)</div>
    <div><b>Approximate Warehouse Area:</b> 9,000 SF (Owner)</div>
    <div class="specs__head">Office Configuration:</div>
    <ul>
      <li>[1] 14' X 16' Executive Office;</li>
      <li>[2] 14' X 12' Offices;</li>
      <li>[1] 10'8" X 12' Office;</li>
      <li>[1] Women's Restroom;</li>
      <li>[1] Men's Restroom;</li>
      <li>[1] Unisex Restroom;</li>
      <li>[1] 21'11" X 13' Conference Room;</li>
      <li>[1] Approximately 29' X 20' Training Room;</li>
      <li>[1] 26' X 11' Expanded Copy/Work Room;</li>
      <li>[1] 14' X 18'8" Break Room;</li>
      <li>[1] 16' X 12' Tech Supervision Room; [Multiple] Storage Closets;</li>
    </ul>
    <div class="specs__head">Warehouse Configuration:</div>
    <ul>
      <li>[3] Grade-Level Loading Doors;</li>
      <li>Approximately 22' Eave Height;</li>
      <li>3-Phase Power;</li>
      <li>Room For Fenced Outside Storage;</li>
      <li>Plenty of Parking;</li>
      <li>Large Dumpster Enclosure;</li>
    </ul>
  </div>
  <div class="plan-note">INTERIOR LAYOUT NOT TO SCALE I DRAWING FOR SAMPLE PURPOSES ONLY</div>
  <footer class="footer">
    <div class="footer__card">
      <div class="footer__badge"><span></span>TALMVEX<br>COMMERCIAL REAL ESTATE</div>
      <div class="footer__contact"><b>WADE T. LORNE</b><br>PRESIDENT | CEO<br><b>PHONE:</b> (281) 555-0148<br><b>E-Mail:</b> Wade@TLMVX.net<br>TREC BROKER LICENSE: 9004417</div>
      <div class="footer__legal">The information contained herein was obtained from sources we believe to be reliable, and we have no reason to doubt its accuracy. All details are submitted subject to errors, omissions or changes in condition prior to sale, lease or withdrawal without notice. Buyers should verify all facts independently. We make no warranty regarding the condition of the property or any environmental matters.</div>
    </div>
  </footer>
</section>

</body>
</html>
```